Looking for awesome business card design with attached existing logo

We are a water, mold, and fire damage restoration company called "Torvane Seco" Looking for an awesome business card that is edgy yet professional and unique. Show me what you got!

```html
<!DOCTYPE html>
<html lang="en">
<head>
<meta charset="utf-8">
<title>Torvane Seco – Business Card</title>
<link href="https://fonts.googleapis.com/css2?family=Montserrat:wght@400;500;700&display=swap" rel="stylesheet">
<style>
  :root {
    --backdrop: #2a2a2c;
    --gold: #d3962e;
    --navy: #2b4a5a;
    --white: #ffffff;
    --card-w: 620px;
    --card-h: 354px;
  }
  * { box-sizing: border-box; margin: 0; padding: 0; }
  html, body { width: 1200px; height: 940px; overflow: hidden; }
  body {
    background: var(--backdrop);
    font-family: "Montserrat", Arial, sans-serif;
    position: relative;
  }
  .card {
    position: absolute;
    width: var(--card-w);
    height: var(--card-h);
    overflow: hidden;
    background: var(--gold);
    box-shadow: 0 14px 30px rgba(0,0,0,.45);
  }
  .card-front { left: 70px; top: 90px; }
  .card-back { left: 510px; top: 490px; }

  .company-name {
    position: absolute;
    font-weight: 500;
    white-space: nowrap;
    letter-spacing: 0;
  }
  .card-front .company-name {
    left: 50%; top: 50%;
    transform: translate(-50%, -50%);
    font-size: 44px;
    color: var(--white);
  }
  .card-back .company-name {
    left: 448px; top: 122px;
    transform: translateX(-50%);
    font-size: 28px;
    color: var(--navy);
  }

  .back-shape { position: absolute; inset: 0; }

  .contact {
    position: absolute; left: 36px; top: 146px;
    color: var(--white);
  }
  .contact-name { font-weight: 700; font-size: 17px; letter-spacing: .02em; text-transform: uppercase; }
  .contact-role { font-size: 13px; margin-top: 3px; }
  .contact-address { font-size: 13px; line-height: 1.4; margin-top: 12px; }
  .contact-list { list-style: none; margin-top: 12px; font-size: 13px; }
  .contact-list li { display: flex; align-items: center; gap: 10px; margin-bottom: 7px; }
  .contact-list svg { width: 15px; height: 15px; flex: none; fill: var(--white); }
</style>
</head>
<body>

<section class="card card-front" aria-label="Card front">
  <p class="company-name">Torvane Seco</p>
</section>

<section class="card card-back" aria-label="Card back">
  <svg class="back-shape" viewBox="0 0 620 354" preserveAspectRatio="none" aria-hidden="true">
    <path fill="var(--navy)" d="M296,0 C222,46 226,142 334,204 C424,256 540,284 620,298 L620,0 Z" transform="translate(2,12)"/>
    <path fill="var(--white)" d="M300,0 C232,42 238,132 338,192 C428,246 540,272 620,284 L620,0 Z"/>
    <path fill="none" stroke="var(--white)" stroke-width="3" d="M286,8 C220,54 226,150 334,214 C424,266 540,292 620,306"/>
  </svg>

  <p class="company-name">Torvane Seco</p>

  <div class="contact">
    <p class="contact-name">Dalen Whitcombe</p>
    <p class="contact-role">Managing Director</p>
    <p class="contact-address">4180 Marlowe Avenue<br>Montreal, QC, H2T1K4</p>
    <ul class="contact-list">
      <li><svg viewBox="0 0 24 24" aria-hidden="true"><path d="M6.6 10.8a15 15 0 0 0 6.6 6.6l2.2-2.2a1 1 0 0 1 1-.25 11.4 11.4 0 0 0 3.6.57 1 1 0 0 1 1 1V20a1 1 0 0 1-1 1A17 17 0 0 1 3 4a1 1 0 0 1 1-1h3.5a1 1 0 0 1 1 1c0 1.25.2 2.450.57 3.57a1 1 0 0 1-.25 1z"/></svg>555-310-2284</li>
      <li><svg viewBox="0 0 24 24" aria-hidden="true"><path d="M2 5h20v14H2zm2 2v.5l8 5 8-5V7zm0 2.8V17h16V9.8l-8 5z"/></svg>info@torvaneseco.com-au</li>
      <li><svg viewBox="0 0 24 24" aria-hidden="true"><path d="M12 2a10 10 0 1 0 0 20 10 10 0 0 0 0-20zm6.9 6h-3a15 15 0 0 0-1.3-3.9A8 8 0 0 1 18.9 8zM12 4a13 13 0 0 1 1.9 4h-3.8A13 13 0 0 1 12 4zM4.3 14a8 8 0 0 1 0-4h3.4a16 16 0 0 0 0 4zm.8 2h3a15 15 0 0 0 1.3 3.9A8 8 0 0 1 5.1 16zm3-8h-3a8 8 0 0 1 4.3-3.9A15 15 0 0 0 8.1 8zM12 20a13 13 0 0 1-1.9-4h3.8A13 13 0 0 1 12 20zm2.3-6H9.7a14 14 0 0 1 0-4h4.6a14 14 0 0 1 0 4zm.3 5.9a15 15 0 0 0 1.3-3.9h3a8 8 0 0 1-4.3 3.9zM16.3 14a16 16 0 0 0 0-4h3.4a8 8 0 0 1 0 4z"/></svg>www.torvaneseco.com-au</li>
    </ul>
  </div>
</section>

</body>
</html>
```